Personal Training Studio Checkin App (or URL based)

I would like a simple web based app built for our  business. We have a training studio with a simple business model. All our clients buy sessions in packages either 4, 8, or 12 at a time. We want something that a trainer can pull up and Check in a client. This will record the date and time the client was checked in, by what trainer, and what type of session. This system will keep track of the following:
Whenever a Client Checks in so it will ‘tick off’ a session on their package (ie- they have gone from 11 sessions left to 10 sessions left)
Track what sessions a particular trainer does so we can pay them at the end of the week and look at who they trained, what type of session and how many
Look at client activity: Every time they check in, Recharge their package, any activity related to the client, even if it was admin – like deleting a session that was mistakenly recorded.
This will keep a database of clients added and all their activity
The pdf I have included lays out how I think it would work and the features I want
I would like this to run off an vornix that we have at our front check in counter. It can be an app or a URL that use.
***THIS PROJECT IS NOT SO MUCH ABOUT DESIGN BUT ABOUT FUNCTIONALITY OF THE APPLICATION. IT MUST HAVE THE FEATURES I HAVE ASKED FOR THAT WORK TOGETHER. I AM WILLING TO PAY A LITTLE MORE AS A BONUS IF YOU CAN ACCOMPLISH THIS. ALSO IF I FIN THE RIGHT PERSON THAT CAN DO THIS I WILL MAKE IT A GUARNTEED PROJECT.

- Functionality and Track and record all the info we need

```html
<!DOCTYPE html>
<html lang="en">
<head>
<meta charset="utf-8">
<title>Formwell Studio Check-In App Screens</title>
<link rel="stylesheet" href="https://fonts.googleapis.com/css2?family=Montserrat:wght@500;600;700;800&family=Open+Sans:wght@400;600&display=swap">
<style>
:root{
  --orange:#ff4f0f;
  --charcoal:#5a5a5a;
  --ink:#2b2b2b;
  --label:#555;
  --field:#f4f4f4;
  --field-line:#e2e2e2;
  --stage:#9a9a9a;
  --card:#ffffff;
  --band:#d6d6d6;
}
*{box-sizing:border-box;margin:0;padding:0}
html,body{width:1200px;height:3884px;overflow:hidden}
body{background:var(--stage);font-family:"Open Sans",Arial,sans-serif;position:relative}
.screen{position:absolute;left:80px;width:1040px;border-radius:34px;overflow:hidden;
  background:linear-gradient(135deg,#ffffff 0%,#f6f6f6 40%,#ffffff 60%,#f2f2f2 100%);
  box-shadow:0 10px 30px rgba(0,0,0,.25)}
.brand{position:absolute;left:0;right:0;text-align:center}
.brand-name{font-family:"Montserrat",Arial,sans-serif;font-weight:800;color:var(--ink);letter-spacing:1px;line-height:1}
.brand-tag{font-family:"Montserrat",Arial,sans-serif;font-weight:600;color:var(--orange);letter-spacing:2px;margin-top:6px}
.pill{position:absolute;height:40px;border-radius:20px;display:flex;align-items:center;justify-content:center;gap:8px;
  font-family:"Montserrat",Arial,sans-serif;font-weight:700;font-size:13px;text-transform:uppercase;letter-spacing:.5px}
.pill svg{width:14px;height:14px}
.pill-dark{background:var(--charcoal);color:#fff}
.pill-orange{background:var(--orange);color:#fff}
.pill-outline{background:#fff;color:var(--ink);border:1.5px solid var(--charcoal)}
.hero-art{position:absolute;left:300px;top:420px;width:480px;height:420px;border-radius:12px;
  background:radial-gradient(ellipse at 60% 50%,#ffe1d4 0%,#f2f2f2 55%,rgba(255,255,255,0) 75%)}
.hero-rule{position:absolute;left:0;right:0;top:808px;height:8px;background:var(--orange)}
.hero-band{position:absolute;left:0;right:0;top:816px;bottom:0;background:var(--band)}
.panel{position:absolute;border:4px solid var(--orange);border-radius:26px}
.panel-title{position:absolute;left:50%;top:-22px;transform:translateX(-50%);background:#fff;padding:0 14px;white-space:nowrap;
  font-family:"Montserrat",Arial,sans-serif;font-weight:700;font-size:32px;color:var(--ink);text-transform:uppercase}
.field{position:absolute}
.field label{display:block;font-size:15px;color:var(--label);margin-bottom:12px}
.input{height:42px;background:var(--field);border:1px solid var(--field-line);border-radius:6px;position:relative}
.input.select::after{content:"";position:absolute;right:12px;top:15px;width:8px;height:8px;
  border-right:2px solid #777;border-bottom:2px solid #777;transform:rotate(45deg)}
.submit{position:absolute;height:48px;border-radius:10px;background:var(--orange);color:#fff;display:flex;align-items:center;justify-content:center;
  font-family:"Montserrat",Arial,sans-serif;font-weight:700;font-size:16px;text-transform:uppercase}
</style>
</head>
<body>

<!-- Home screen -->
<section class="screen" style="top:80px;height:880px">
  <div class="brand" style="top:160px">
    <div class="brand-name" style="font-size:84px">FORMWELL</div>
    <div class="brand-tag" style="font-size:22px">PERSONAL TRAINING STUDIO</div>
  </div>
  <div class="pill pill-dark" style="left:140px;top:328px;width:240px">
    <svg viewBox="0 0 14 14"><circle cx="7" cy="4" r="3" fill="#fff"/><path d="M1 14c0-4 3-6 6-6s6 2 6 6z" fill="#fff"/></svg>Client Check In</div>
  <div class="pill pill-orange" style="left:412px;top:328px;width:268px">
    <svg viewBox="0 0 14 14"><circle cx="5" cy="4" r="3" fill="#fff"/><path d="M0 14c0-4 2-6 5-6s5 2 5 6z" fill="#fff"/><path d="M11 4v6M8 7h6" stroke="#fff" stroke-width="1.6"/></svg>Add New Client</div>
  <div class="pill pill-outline" style="left:700px;top:328px;width:200px">
    <svg viewBox="0 0 14 14"><circle cx="7" cy="7" r="5" fill="none" stroke="#444" stroke-width="1.6"/><circle cx="7" cy="7" r="2" fill="#444"/></svg>Admin Panel</div>
  <div class="hero-art" role="img" aria-label="Illustration of a trainer holding a checked-off session form"></div>
  <div class="hero-rule"></div>
  <div class="hero-band"></div>
</section>

<!-- Client check in -->
<section class="screen" style="top:1020px;height:860px">
  <div class="brand" style="top:40px">
    <div class="brand-name" style="font-size:40px">FORMWELL</div>
    <div class="brand-tag" style="font-size:11px">PERSONAL TRAINING STUDIO</div>
  </div>
  <div class="panel" style="left:260px;top:188px;width:520px;height:512px">
    <div class="panel-title">Client Check In</div>
    <div class="field" style="left:36px;top:38px;width:440px"><label>Client Name:</label><div class="input select"></div></div>
    <div class="field" style="left:36px;top:132px;width:440px"><label>Trainer Name:</label><div class="input select"></div></div>
    <div class="field" style="left:36px;top:226px;width:440px"><label>Session Type:</label><div class="input select"></div></div>
    <div class="field" style="left:36px;top:320px;width:440px"><label>Partner Name:</label><div class="input"></div></div>
    <div class="submit" style="left:36px;top:424px;width:440px">Submit Now</div>
  </div>
</section>

<!-- Add client -->
<section class="screen" style="top:1960px;height:880px">
  <div class="brand" style="top:28px">
    <div class="brand-name" style="font-size:40px">FORMWELL</div>
    <div class="brand-tag" style="font-size:11px">PERSONAL TRAINING STUDIO</div>
  </div>
  <div class="panel" style="left:232px;top:120px;width:576px;height:708px">
    <div class="panel-title">Add Client Panel</div>
    <div class="field" style="left:36px;top:42px;width:206px"><label>First Name:</label><div class="input"></div></div>
    <div class="field" style="left:254px;top:42px;width:206px"><label>Last Name:</label><div class="input"></div></div>
    <div class="field" style="left:36px;top:134px;width:206px"><label>Email:</label><div class="input"></div></div>
    <div class="field" style="left:254px;top:134px;width:206px"><label>Phone:</label><div class="input"></div></div>
    <div class="field" style="left:36px;top:226px;width:496px"><label>Session Type:</label><div class="input select"></div></div>
    <div class="field" style="left:36px;top:318px;width:424px"><label>Starting Package Session Amount:</label><div class="input"></div></div>
    <div class="field" style="left:36px;top:412px;width:206px"><label>Partner First Name:</label><div class="input"></div></div>
    <div class="field" style="left:254px;top:412px;width:206px"><label>Partner Last Name:</label><div class="input"></div></div>
    <div class="field" style="left:36px;top:504px;width:206px"><label>Email:</label><div class="input"></div></div>
    <div class="field" style="left:254px;top:504px;width:206px"><label>Phone:</label><div class="input"></div></div>
    <div class="submit" style="left:36px;top:612px;width:496px">Submit Now</div>
  </div>
</section>

<!-- Admin panel -->
<section class="screen" style="top:2908px;height:892px">
  <div class="brand" style="top:48px">
    <div class="brand-name" style="font-size:40px">FORMWELL</div>
    <div class="brand-tag" style="font-size:11px">PERSONAL TRAINING STUDIO</div>
  </div>
  <div class="panel" style="left:232px;top:200px;width:576px;height:480px">
    <div class="panel-title" style="top:-2px;padding-top:22px;background:transparent">Admin Panel</div>
    <div class="pill pill-dark" style="left:188px;top:96px;width:200px;height:36px">
      <svg viewBox="0 0 14 14"><circle cx="7" cy="4" r="3" fill="#fff"/><path d="M1 14c0-4 3-6 6-6s6 2 6 6z" fill="#fff"/></svg>Add Client</div>
    <div class="pill pill-orange" style="left:188px;top:164px;width:200px;height:36px">
      <svg viewBox="0 0 14 14"><rect x="2" y="1" width="10" height="12" rx="1" fill="#fff"/><path d="M4 5h6M4 8h6" stroke="#ff4f0f" stroke-width="1.4"/></svg>Client Details</div>
    <div class="pill pill-outline" style="left:188px;top:232px;width:200px;height:36px">
      <svg viewBox="0 0 14 14"><path d="M1 12l4-5 3 3 5-7" fill="none" stroke="#444" stroke-width="1.6"/></svg>Trainer Report</div>
    <div class="pill pill-dark" style="left:188px;top:300px;width:200px;height:36px">
      <svg viewBox="0 0 14 14"><rect x="1" y="3" width="12" height="9" rx="1" fill="#fff"/></svg>Trainer Panel</div>
    <div class="pill pill-orange" style="left:188px;top:368px;width:200px;height:36px">
      <svg viewBox="0 0 14 14"><circle cx="7" cy="7" r="6" fill="#fff"/><path d="M7 3v4l3 2" fill="none" stroke="#ff4f0f" stroke-width="1.4"/></svg>Session Report</div>
  </div>
</section>

</body>
</html>
```